Gala Event Program - Italian

Need a program with the exact same layout/structure as attached. The new theme for the event this year will be: Notte di Lanterne Dorate, Under Golden Lantern Light. The look that we are going for is Italian garden party. The page sizes should also be the same as previously - 8.5 X 11.

The image sizes relative to pring should remain roughly the same for the individual and group pages.

```html
<!DOCTYPE html>
<html lang="en">
<head>
<meta charset="utf-8">
<title>Executive Board of Directors</title>
<link href="https://fonts.googleapis.com/css2?family=Roboto:wght@300;400;700&family=Great+Vibes&family=Pinyon+Script&family=Baloo+2:wght@700&display=swap" rel="stylesheet">
<style>
  :root {
    --orange-deep: #c65a12;
    --orange-light: #f7a84a;
    --ink: #111111;
    --paper: #ffffff;
    --blossom: #f2a7bf;
    --blossom-deep: #e57a98;
    --leaf: #3d5a2e;
    --halo: #aac4ff;
  }
  html, body { margin: 0; padding: 0; overflow: hidden; background: var(--paper); }
  .page {
    position: relative;
    width: 927px;
    height: 1200px;
    overflow: hidden;
    background: var(--paper);
    font-family: "Roboto", Arial, sans-serif;
    color: var(--ink);
  }
  .frame { position: absolute; inset: 0; }
  .floral-corner { position: absolute; }
  .floral-corner--top { left: 52px; top: 30px; width: 282px; height: 248px; }
  .floral-corner--bottom { left: 558px; top: 824px; width: 306px; height: 304px; }

  .title {
    position: absolute;
    left: 0; right: 0;
    text-align: center;
  }
  .title__main {
    position: absolute;
    left: 406px; width: 300px;
    top: 54px;
    text-align: center;
    font-weight: 400;
    font-size: 52px;
    line-height: 1;
    letter-spacing: 0.5px;
    background: linear-gradient(180deg, var(--orange-light), var(--orange-deep));
    -webkit-background-clip: text;
    background-clip: text;
    color: transparent;
  }
  .title__sub {
    position: absolute;
    left: 406px; width: 300px;
    top: 96px;
    text-align: center;
    font-family: "Pinyon Script", cursive;
    font-size: 34px;
    line-height: 1;
  }

  .section-heading {
    position: absolute;
    width: 200px;
    text-align: center;
    font-family: "Great Vibes", cursive;
    font-size: 54px;
    line-height: 1;
  }
  .section-heading--officer { left: 413px; top: 232px; }
  .section-heading--patron { left: 403px; top: 590px; }

  .roster {
    position: absolute;
    font-size: 21px;
    line-height: 25.4px;
  }
  .roster__col { position: absolute; top: 0; white-space: nowrap; }
  .roster__col--left { right: 0; text-align: right; }
  .roster__col--right { left: 0; }
  .roster__role { font-weight: 700; }

  .roster--officer { left: 0; top: 327px; width: 927px; }
  .roster--officer .roster__col--left { right: 443px; }
  .roster--officer .roster__col--right { left: 516px; }

  .roster--patron { left: 0; top: 678px; width: 927px; }
  .roster--patron .roster__col--left { right: 446px; }
  .roster--patron .roster__col--right { left: 516px; }

  .page-number {
    position: absolute;
    left: 410px; top: 1071px;
    width: 72px; height: 72px;
    line-height: 72px;
    text-align: center;
    font-family: "Baloo 2", sans-serif;
    font-weight: 700;
    font-size: 30px;
    color: var(--orange-deep);
  }
</style>
</head>
<body>
<div class="page">
  <svg class="frame" width="927" height="1200" viewBox="0 0 927 1200" aria-hidden="true">
    <defs>
      <linearGradient id="frameGradient" x1="0" y1="0" x2="927" y2="1200" gradientUnits="userSpaceOnUse">
        <stop offset="0" stop-color="var(--orange-deep)"/>
        <stop offset="0.5" stop-color="var(--orange-light)"/>
        <stop offset="1" stop-color="var(--orange-deep)"/>
      </linearGradient>
      <radialGradient id="haloGradient" cx="0.5" cy="0.5" r="0.5">
        <stop offset="0.75" stop-color="#ffffff"/>
        <stop offset="1" stop-color="var(--halo)"/>
      </radialGradient>
    </defs>
    <g fill="none" stroke="url(#frameGradient)" stroke-width="3.5" stroke-linecap="round">
      <path d="M414,62 a7,7 0 1 1 -6,-11 a13,13 0 0 1 12,-14 H866 V825 a15,15 0 0 1 -17,15 a8,8 0 1 1 7,-11"/>
      <path d="M82,318 a7,7 0 1 0 -6,-11 a13,13 0 0 0 -17,15 V1107 H540 a15,15 0 0 0 15,-17 a8,8 0 1 0 -11,7"/>
    </g>
    <g class="page-badge">
      <circle cx="446" cy="1107" r="37" fill="url(#haloGradient)"/>
      <path d="M404,1093 a45,45 0 0 1 84,0" fill="none" stroke="url(#frameGradient)" stroke-width="2"/>
      <path d="M404,1121 a45,45 0 0 0 84,0" fill="none" stroke="url(#frameGradient)" stroke-width="2"/>
      <circle cx="401" cy="1093" r="3" fill="var(--orange-deep)"/>
      <circle cx="491" cy="1093" r="3" fill="var(--orange-deep)"/>
      <circle cx="401" cy="1121" r="3" fill="var(--orange-deep)"/>
      <circle cx="491" cy="1121" r="3" fill="var(--orange-deep)"/>
    </g>
    <g class="heading-rules" fill="var(--ink)" stroke="var(--ink)" stroke-width="1.6">
      <line x1="454" y1="297" x2="570" y2="297"/>
      <circle cx="454" cy="297" r="3"/><circle cx="570" cy="297" r="3"/>
      <line x1="444" y1="643" x2="562" y2="643"/>
      <circle cx="444" cy="643" r="3"/><circle cx="562" cy="643" r="3"/>
    </g>
    <g class="heading-blossoms">
      <circle cx="425" cy="297" r="17" fill="var(--blossom)" role="img" aria-label="Small pink blossom illustration"/>
      <circle cx="600" cy="297" r="17" fill="var(--blossom)" role="img" aria-label="Small pink blossom illustration"/>
      <circle cx="416" cy="643" r="17" fill="var(--blossom)" role="img" aria-label="Small pink blossom illustration"/>
      <circle cx="591" cy="643" r="17" fill="var(--blossom)" role="img" aria-label="Small pink blossom illustration"/>
    </g>
  </svg>

  <svg class="floral-corner floral-corner--top" viewBox="0 0 282 248" role="img" aria-label="Illustration of pink and cream blossoms with green leaves">
    <defs>
      <radialGradient id="bloomTop" cx="0.4" cy="0.55" r="0.6">
        <stop offset="0" stop-color="var(--blossom-deep)"/>
        <stop offset="0.55" stop-color="var(--blossom)"/>
        <stop offset="1" stop-color="var(--leaf)" stop-opacity="0.35"/>
      </radialGradient>
    </defs>
    <ellipse cx="141" cy="124" rx="141" ry="124" fill="url(#bloomTop)" opacity="0.55"/>
  </svg>

  <svg class="floral-corner floral-corner--bottom" viewBox="0 0 306 304" role="img" aria-label="Illustration of pink blossoms with dark green leaves">
    <defs>
      <radialGradient id="bloomBottom" cx="0.5" cy="0.7" r="0.6">
        <stop offset="0" stop-color="var(--blossom-deep)"/>
        <stop offset="0.5" stop-color="var(--blossom)"/>
        <stop offset="1" stop-color="var(--leaf)" stop-opacity="0.35"/>
      </radialGradient>
    </defs>
    <ellipse cx="153" cy="152" rx="153" ry="152" fill="url(#bloomBottom)" opacity="0.55"/>
  </svg>

  <h1 class="title__main" style="margin:0">EXECUTIVE</h1>
  <div class="title__sub">Board of Directors</div>

  <h2 class="section-heading section-heading--officer" style="margin:0;font-weight:400">Officer</h2>
  <div class="roster roster--officer">
    <div class="roster__col roster__col--left roster__role">
      President<br>President Elect<br>VP Membership<br>VP Projects<br>Recording Secretary<br>Treasurer<br>Parliamentarian<br>Corresponding Secretary
    </div>
    <div class="roster__col roster__col--right">
      Marina Calloway<br>Tessa Marlowe<br>Paula Wrenfield<br>Gianna Rossetti<br>Celia Navarre<br>Laurel Pike<br>Nora Halvers<br>Josephine Ardley
    </div>
  </div>

  <h2 class="section-heading section-heading--patron" style="margin:0;font-weight:400">Patron</h2>
  <div class="roster roster--patron">
    <div class="roster__col roster__col--left">
      Dara Ellison<br>Miriam Thackery<br>Renata Bellamy<br>Clara Hensley<br>Lucia Pembrook<br>Valerie Lindqvist<br>Katia Morrow
    </div>
    <div class="roster__col roster__col--right">
      Edith R. Corwin<br>Sylvia Dunmore<br>Tina Ashgrove<br>Greta Fallon<br>Bryony Hale<br>Ivy Keller
    </div>
  </div>

  <div class="page-number">03</div>
</div>
</body>
</html>
```